Mental Health care Company in Washington DC

We are a new mental health care services provider in Washington DC. Please look at these sites.
https://marlowbrookpartners.com
https://www.quillstoneinc.com
https://velmarsh-kt.org/
https://www.trivanqx.com
https://www.thelanternofqz.com

```html
<!DOCTYPE html>
<html lang="en">
<head>
<meta charset="utf-8">
<title>Harborlight Health Services</title>
<link href="https://fonts.googleapis.com/css2?family=IBM+Plex+Sans:wght@400;600;700&family=Poppins:wght@300;400;500;600&display=swap" rel="stylesheet">
<style>
:root{
  --navy:#0d1f3c;
  --orange:#f5a262;
  --teal:#a3dde0;
  --teal-dark:#7fcdd2;
  --cream:#faf3ee;
  --mist:#eff7f8;
  --text:#2b2f3a;
  --white:#ffffff;
}
*{box-sizing:border-box;margin:0;padding:0}
html,body{width:1200px;height:3763px;overflow:hidden}
body{position:relative;background:var(--white);font-family:'Poppins',sans-serif;color:var(--text)}
.abs{position:absolute}
.heading{font-family:'IBM Plex Sans',sans-serif;font-weight:700;color:var(--navy);letter-spacing:1px}
.btn{position:absolute;display:flex;align-items:center;justify-content:center;background:var(--orange);color:var(--white);font-weight:500;font-size:14px;border-radius:0 24px 24px 24px;letter-spacing:.3px}

/* top bar */
.topbar{left:0;top:0;width:1200px;height:46px;background:var(--navy);color:var(--white);font-size:14px;font-weight:500}
.topbar .item{position:absolute;top:8px;display:flex;align-items:center;gap:14px}
.ring{width:30px;height:30px;border-radius:50%;border:1.5px solid #5b6c86;display:flex;align-items:center;justify-content:center}
.socials{position:absolute;display:flex;gap:8px}
.socials span{width:28px;height:28px;border-radius:50%;border:1.5px solid #c8cfd9}
.socials span.on{background:var(--orange);border-color:var(--orange)}

/* header */
.brand{font-family:'Poppins',sans-serif;font-weight:500;color:var(--navy);font-size:31px;display:flex;align-items:center;gap:10px;white-space:nowrap}
.brand i{width:14px;height:14px;border-radius:50%;background:var(--orange);display:block}
.brand.small{font-size:22px;gap:8px}
.brand.small i{width:11px;height:11px}
.nav{top:92px;font-size:14px;font-weight:500;color:var(--navy)}
.nav.active{color:var(--teal-dark);border-bottom:1px solid var(--teal-dark)}

/* hero */
.hero-title{left:111px;top:348px;color:var(--white);font-family:'IBM Plex Sans',sans-serif;font-size:44px;line-height:54px;letter-spacing:1px}
.hero-title b{font-weight:700}
.hero-title span{font-weight:400}
.hero-sub{left:111px;top:462px;color:var(--white);font-size:22px}
.dots{left:558px;top:728px;display:flex;gap:10px}
.dots span{width:13px;height:13px;border-radius:50%;border:2px solid var(--white)}
.dots span.on{background:var(--orange);border-color:var(--orange)}

/* services */
.card{position:absolute;width:477px;height:231px;background:var(--cream);border-radius:24px 0 40px 24px}
.card .photo{position:absolute;left:7px;top:7px;width:223px;height:217px;border-radius:18px 0 28px 0}
.card h3{position:absolute;left:258px;top:26px;font-size:17px;font-weight:600;color:var(--navy)}
.card p{position:absolute;left:258px;top:58px;width:200px;font-size:13.5px;line-height:22.5px;color:var(--text)}
.card .btn{left:258px;top:158px;width:136px;height:41px;font-size:13px}
.card.feature{background:var(--orange)}
.card.feature h3,.card.feature p{color:var(--white)}
.card.feature .btn{background:var(--white);color:var(--navy)}

/* about */
.about-text{left:657px;top:1572px;width:432px}
.about-text h2{font-size:36px;line-height:46px;white-space:nowrap}
.about-text p{margin-top:14px;font-size:15.5px;line-height:25px;text-align:justify;color:var(--text)}
.about-text p:first-of-type{margin-top:20px}
.about-text .btn{position:static;width:147px;height:44px;margin-top:26px}

/* testimonial */
.testi{left:150px;top:2314px;width:900px;height:412px;border-radius:60px;overflow:hidden;background:var(--mist)}
.testi .photo{position:absolute;left:450px;top:0;width:450px;height:412px}
.quote{left:44px;top:42px;font-family:'IBM Plex Sans',sans-serif;font-size:110px;line-height:1;color:var(--teal-dark);font-weight:700}
.who{left:44px;top:98px;font-size:16px;color:var(--navy)}
.who b{font-weight:600}
.stars{left:44px;top:126px;display:flex;gap:3px}
.testi p{position:absolute;left:44px;width:360px;font-size:16.5px;line-height:25.5px;color:var(--text)}

/* contact */
.contact-title{left:111px;top:2930px;color:var(--white);font-size:46px}
.field{position:absolute;background:var(--white);display:flex;align-items:flex-start;gap:8px;padding:12px 14px;font-size:14px;color:#4c4f58}
.field svg{flex:none;margin-top:3px}
.send{left:413px;top:3238px;width:184px;height:47px;background:var(--teal);color:var(--navy);border-radius:24px 0 24px 24px}

/* footer */
.fcol h4{font-size:16px;font-weight:500;color:var(--navy);margin-bottom:14px;letter-spacing:.3px}
.fcol li{list-style:none;font-size:13.5px;line-height:28.5px;color:#3b3f4a}
.info{display:flex;gap:18px;font-size:13.5px;line-height:25px;color:#3b3f4a;margin-bottom:6px}
.info .ico{width:26px;height:26px;border-radius:50%;background:#fdf0e6;flex:none;display:flex;align-items:center;justify-content:center}
.rule{left:111px;top:3708px;width:978px;height:1px;background:#e3e6ea}
.copy{left:505px;top:3722px;font-size:13px;color:#4c4f58}
</style>
</head>
<body>

<!-- top bar -->
<div class="abs topbar">
  <div class="item" style="left:146px">
    <span class="ring"><svg width="12" height="12" viewBox="0 0 24 24" fill="#f5a262"><path d="M6.6 10.8a15 15 0 0 0 6.6 6.6l2.2-2.2a1 1 0 0 1 1-.25 11.4 11.4 0 0 0 3.6.57 1 1 0 0 1 1 1V20a1 1 0 0 1-1 1A17 17 0 0 1 3 4a1 1 0 0 1 1-1h3.5a1 1 0 0 1 1 1c0 1.25.2 2.45.57 3.6a1 1 0 0 1-.25 1z"/></svg></span>202-555-0148
  </div>
  <div class="item" style="left:322px">
    <span class="ring"><svg width="13" height="10" viewBox="0 0 24 18" fill="#f5a262"><path d="M0 0h24v18H0z M2 2l10 7 10-7" stroke="#0d1f3c" stroke-width="2"/></svg></span>hello@harborlighthealth.com
  </div>
  <div class="socials" style="left:908px;top:8px"><span></span><span></span><span class="on"></span><span></span></div>
</div>

<!-- header -->
<div class="abs brand" style="left:111px;top:76px">Harborlight Health <i></i></div>
<div class="abs nav active" style="left:530px">HOME</div>
<div class="abs nav" style="left:609px">ABOUT US</div>
<div class="abs nav" style="left:717px">SERVICES</div>
<div class="abs nav" style="left:823px">BLOG</div>
<div class="btn" style="left:904px;top:79px;width:150px;height:47px">CONTACT US</div>

<!-- hero -->
<svg class="abs" style="left:0;top:153px" width="1200" height="618" role="img" aria-label="Photograph of two hikers sitting on a rocky mountain top overlooking a lake at sunset">
  <defs>
    <linearGradient id="heroGrad" x1="0" y1="0" x2="1" y2="1">
      <stop offset="0" stop-color="#b98658"/>
      <stop offset=".45" stop-color="#8a6a57"/>
      <stop offset="1" stop-color="#4c4149"/>
    </linearGradient>
  </defs>
  <path d="M1200 0 C1200 330 930 618 560 618 L0 618 L0 330 C0 140 220 0 560 0 Z" fill="url(#heroGrad)"/>
</svg>
<div class="abs hero-title"><b>WHERE HEALING BEGINS</b><br><span>AND HOPE GROWS</span></div>
<div class="abs hero-sub">Your Trusted Partner in Mental Wellness</div>
<div class="btn" style="left:111px;top:517px;width:236px;height:47px">BOOK AN APPOINTMENT</div>
<div class="abs dots"><span></span><span class="on"></span><span></span><span></span></div>

<!-- services -->
<h2 class="abs heading" style="left:0;width:1200px;text-align:center;top:852px;font-size:48px">OUR SERVICES</h2>

<div class="card" style="left:111px;top:943px">
  <div class="photo" role="img" aria-label="Photograph of a therapist taking notes with a client" style="background:linear-gradient(135deg,#e9ecee,#b9c2c8)"></div>
  <h3>Individual Therapy</h3>
  <p>One-on-one sessions to explore personal challenges and develop coping strategies.</p>
  <div class="btn">LEARN MORE</div>
</div>
<div class="card" style="left:613px;top:943px">
  <div class="photo" role="img" aria-label="Photograph of a family walking together at sunset" style="background:linear-gradient(160deg,#f7e2c2,#e0a877)"></div>
  <h3>Family Counseling</h3>
  <p>Sessions aimed at improving communication and resolving conflicts within families.</p>
  <div class="btn">LEARN MORE</div>
</div>
<div class="card feature" style="left:111px;top:1197px">
  <div class="photo" role="img" aria-label="Photograph of a supportive group therapy session" style="background:linear-gradient(135deg,#d9d6d4,#8a7d75)"></div>
  <h3>Group Therapy</h3>
  <p>Facilitated group sessions that provide community support and shared learning.</p>
  <div class="btn">LEARN MORE</div>
</div>
<div class="card" style="left:613px;top:1197px">
  <div class="photo" role="img" aria-label="Photograph of a woman talking on a sofa beside a plant" style="background:linear-gradient(135deg,#ecebe7,#a9a59c)"></div>
  <h3>Crisis Intervention</h3>
  <p>Immediate support for individuals experiencing acute mental health crises.</p>
  <div class="btn">LEARN MORE</div>
</div>

<!-- about -->
<svg class="abs" style="left:0;top:1511px" width="1200" height="600" role="img" aria-label="Photograph of a calm profile blended with a tree at sunrise beside a teal panel">
  <defs>
    <clipPath id="aboutClip"><path d="M0 600 L0 380 C0 170 260 0 600 0 L880 0 C1060 0 1200 140 1200 300 C1200 470 1060 600 880 600 Z"/></clipPath>
    <linearGradient id="aboutGrad" x1="0" y1="0" x2="1" y2="1">
      <stop offset="0" stop-color="#c7b48f"/><stop offset=".5" stop-color="#6f5a4c"/><stop offset="1" stop-color="#3b3438"/>
    </linearGradient>
  </defs>
  <g clip-path="url(#aboutClip)">
    <rect x="0" y="0" width="600" height="600" fill="url(#aboutGrad)"/>
    <rect x="600" y="0" width="600" height="600" fill="#a3dde0"/>
  </g>
</svg>
<div class="abs about-text">
  <h2 class="heading">ABOUT<br>HARBORLIGHT HEALTH</h2>
  <p>Welcome to Harborlight Health Services, your trusted partner in mental health and wellness. We are dedicated to providing compassionate, client-centered care to individuals across Washington, DC.</p>
  <p>At Harborlight Health Services, our mission is to empower individuals to achieve optimal mental health through personalized care, evidence-based practices, and unwavering support. We are committed to fostering a safe and inclusive environment where every client feels heard, valued, and supported.</p>
  <div class="btn">LEARN MORE</div>
</div>

<!-- testimonials -->
<h2 class="abs heading" style="left:0;width:1200px;text-align:center;top:2216px;font-size:48px">TESTIMONIALS</h2>
<div class="abs testi">
  <div class="abs quote">&ldquo;</div>
  <div class="abs who"><b>&ndash; MARIANNE,</b> Washington, DC</div>
  <div class="abs stars">
    <svg width="60" height="12" viewBox="0 0 60 12" fill="#f5a262"><g id="st"><path d="M6 0l1.8 3.8 4.2.5-3.1 2.9.8 4.1L6 9.2 2.3 11.3l.8-4.1L0 4.3l4.2-.5z"/></g><use href="#st" x="12"/><use href="#st" x="24"/><use href="#st" x="36"/><use href="#st" x="48"/></svg>
  </div>
  <p style="top:160px">Sed ut perspiciatis unde omnis iste natus error sit voluptatem accusantium doloremque laudantium, totam rem aperiam, eaque ipsa quae ab illo inventore dicta sunt explicabo.</p>
  <p style="top:297px">Sed ut perspiciatis unde omnis iste natus error sit voluptatem accusantium doloremque laudantiumea.</p>
  <div class="photo" role="img" aria-label="Photograph of a smiling client" style="background:linear-gradient(135deg,#efe9e2,#cdbfae)"></div>
</div>

<!-- contact -->
<svg class="abs" style="left:0;top:2837px" width="1200" height="555" role="img" aria-label="Photograph of a person meditating on a hilltop in warm golden light">
  <defs>
    <linearGradient id="contactGrad" x1="0" y1="0" x2="1" y2="1">
      <stop offset="0" stop-color="#f7b25b"/><stop offset=".5" stop-color="#ea8a3a"/><stop offset="1" stop-color="#9c4a2a"/>
    </linearGradient>
  </defs>
  <path d="M1200 0 C1200 300 960 555 560 555 L0 555 L0 260 C0 110 180 0 420 0 Z" fill="url(#contactGrad)"/>
</svg>
<h2 class="abs heading contact-title">CONTACT US</h2>
<div class="field" style="left:111px;top:3012px;width:239px;height:44px"><svg width="10" height="12" viewBox="0 0 10 12" fill="#a3dde0"><circle cx="5" cy="3" r="3"/><path d="M0 12a5 5 0 0 1 10 0z"/></svg>First Name</div>
<div class="field" style="left:358px;top:3012px;width:239px;height:44px"><svg width="10" height="12" viewBox="0 0 10 12" fill="#a3dde0"><circle cx="5" cy="3" r="3"/><path d="M0 12a5 5 0 0 1 10 0z"/></svg>Last Name</div>
<div class="field" style="left:111px;top:3066px;width:239px;height:44px"><svg width="13" height="10" viewBox="0 0 13 10" fill="#a3dde0"><rect width="13" height="10" rx="1"/></svg>Email Address</div>
<div class="field" style="left:358px;top:3066px;width:239px;height:44px"><svg width="11" height="11" viewBox="0 0 24 24" fill="#a3dde0"><path d="M6.6 10.8a15 15 0 0 0 6.6 6.6l2.2-2.2a1 1 0 0 1 1-.25 11.4 11.4 0 0 0 3.6.57 1 1 0 0 1 1 1V20a1 1 0 0 1-1 1A17 17 0 0 1 3 4a1 1 0 0 1 1-1h3.5a1 1 0 0 1 1 1c0 1.25.2 2.45.57 3.6a1 1 0 0 1-.25 1z"/></svg>Phone Number</div>
<div class="field" style="left:111px;top:3120px;width:486px;height:104px"><svg width="13" height="11" viewBox="0 0 13 11" fill="#a3dde0"><ellipse cx="6.5" cy="4.5" rx="6.5" ry="4.5"/><path d="M2 11l2-4h3z"/></svg>Leave Message</div>
<div class="btn send">SEND MESSAGE</div>

<!-- footer -->
<div class="abs brand small" style="left:111px;top:3552px">Harborlight Health <i></i></div>
<div class="abs fcol" style="left:385px;top:3460px">
  <h4>QUICK LINKS</h4>
  <ul><li>Home</li><li>About Us</li><li>Services</li><li>Blog</li><li>Contact Us</li><li>Privacy Policy</li><li>Terms &amp; Conditions</li></ul>
</div>
<div class="abs fcol" style="left:569px;top:3460px;width:260px">
  <h4>CONTACT INFO</h4>
  <div class="info"><span class="ico"><svg width="10" height="10" viewBox="0 0 24 24" fill="#f5a262"><path d="M6.6 10.8a15 15 0 0 0 6.6 6.6l2.2-2.2a1 1 0 0 1 1-.25 11.4 11.4 0 0 0 3.6.57 1 1 0 0 1 1 1V20a1 1 0 0 1-1 1A17 17 0 0 1 3 4a1 1 0 0 1 1-1h3.5a1 1 0 0 1 1 1c0 1.25.2 2.45.57 3.6a1 1 0 0 1-.25 1z"/></svg></span>202-555-0148</div>
  <div class="info"><span class="ico"><svg width="11" height="8" viewBox="0 0 11 8" fill="#f5a262"><rect width="11" height="8" rx="1"/></svg></span>hello@harborlighthealth.com</div>
  <div class="info"><span class="ico"><svg width="9" height="12" viewBox="0 0 9 12" fill="#f5a262"><path d="M4.5 0A4.5 4.5 0 0 0 0 4.5C0 8 4.5 12 4.5 12S9 8 9 4.5A4.5 4.5 0 0 0 4.5 0z"/></svg></span>4180 Linden Avenue NW,<br>Suite 210 Washington, DC 20015</div>
  <div class="info"><span class="ico"><svg width="11" height="10" viewBox="0 0 11 10" fill="#f5a262"><rect y="3" width="11" height="7" rx="1"/><rect x="2" width="7" height="3"/></svg></span>202-555-0193</div>
</div>
<div class="abs fcol" style="left:837px;top:3460px;width:260px">
  <h4>OPENING HOURS</h4>
  <div class="info"><span class="ico"><svg width="11" height="11" viewBox="0 0 12 12" fill="none" stroke="#f5a262" stroke-width="1.5"><circle cx="6" cy="6" r="5"/><path d="M6 3v3h2"/></svg></span><span style="line-height:23px">Mon - Fri: 09:00 am &ndash; 05:00 pm<br>Sat: 10:00 am &ndash; 02:00 pm<br>Sun: Closed</span></div>
</div>
<div class="abs rule"></div>
<div class="abs copy">&copy; 2025 &nbsp;/&nbsp; All Rights Reserved</div>
<div class="socials" style="left:942px;top:3722px">
  <span style="border-color:#a3dde0"></span><span style="border-color:#a3dde0"></span><span class="on"></span><span style="border-color:#a3dde0"></span>
</div>

</body>
</html>
```